Brisk Meadow Builders needs a product brochure

We need a new flyer for our Patio Perch Lounge. Here is some of the copy your will need.
"Turn your back yard into the ultimate entertianment venue with the stunning Patio Perch Lounge!"
"Entertain family & friends in your very own back yard!"
"Available with or without solar and comes in a variety of colors"
"The Patio Perch Lounge measures 5' deep by 10' wide and is 9'-6" at it's highest point"
"Constructed with treated 4x4's, primed then painted with Thornby Calder best exterior paint for years of care free enjoyment. Also, Marlow Pendt Keystead shingles are dimensional, have a 25 year warranty and are rated for 150 mph winds!"
"TV Mount included. Shelves and TV are sold separately"
There also needs to be a box where we can add the price into later. The price can change from time to time due to material cost fluctuation.
Look and feel
Each slider illustrates characteristics of the customer's brand and the style your logo design should communicate.

```html
<!DOCTYPE html>
<html lang="en">
<head>
<meta charset="utf-8">
<title>Brisk Meadow Builders – Patio Perch Lounge Flyer</title>
<link href="https://fonts.googleapis.com/css2?family=Montserrat:wght@500;600;700;800&display=swap" rel="stylesheet">
<style>
  :root {
    --green: #4a9a35;
    --orange: #eca524;
    --ink: #1d1d1f;
    --paper: #f6f3f6;
    --backdrop: #e4e2e0;
    --grass-a: #9fb57a;
    --grass-b: #d9ddd0;
    --wood: #6b4a2f;
    --charcoal: #2b2e33;
  }
  * { margin: 0; padding: 0; box-sizing: border-box; }
  html, body { width: 1200px; height: 800px; overflow: hidden; }
  body {
    background: var(--backdrop);
    font-family: "Montserrat", sans-serif;
    color: var(--ink);
    position: relative;
  }
  .flyer {
    position: absolute;
    left: 330px; top: 18px;
    width: 540px; height: 764px;
    background: var(--paper);
    overflow: hidden;
    box-shadow: 0 6px 24px rgba(0,0,0,.18);
  }
  .flyer > * { position: absolute; }
  .hero-scene {
    left: 0; top: 0; width: 540px; height: 420px;
    background: linear-gradient(160deg, var(--grass-a) 0%, #c2cfa8 40%, var(--grass-b) 75%, #ebebea 100%);
  }
  .curves { left: 0; top: 0; width: 540px; height: 764px; }
  .bar-photo {
    left: 275px; top: 36px; width: 245px; height: 300px;
    background: linear-gradient(180deg, var(--charcoal) 0%, #5a4634 45%, var(--wood) 60%, #3a3d42 100%);
    clip-path: polygon(20% 0, 80% 0, 100% 22%, 100% 100%, 0 100%, 0 22%);
  }
  .shelf-photo {
    left: 330px; top: 236px; width: 185px; height: 140px;
    background: linear-gradient(180deg, #3b4a5c 0%, #2b2e33 55%, #4b5058 100%);
    border: 3px solid #fff;
  }
  .brand {
    left: 24px; top: 120px;
    display: flex; align-items: center; gap: 7px;
    font-weight: 700; font-size: 14px; color: var(--green);
    white-space: nowrap;
  }
  .brand-dot { width: 12px; height: 12px; border-radius: 50%; background: var(--orange); }
  .headline {
    left: 30px; top: 222px; width: 240px;
    font-weight: 800; font-size: 18px; line-height: 24px;
    white-space: nowrap;
  }
  .headline .g { color: var(--green); display: block; }
  .headline .o { color: var(--orange); display: block; }
  .features { left: 30px; top: 420px; width: 220px; list-style: none; }
  .features li {
    display: flex; gap: 8px; align-items: flex-start;
    font-weight: 700; font-size: 10.5px; line-height: 14px; margin-bottom: 12px;
  }
  .features svg { flex: none; margin-top: 1px; }
  .specs {
    left: 272px; top: 390px; width: 248px;
    text-align: center; font-weight: 600; font-size: 10px; line-height: 14px;
  }
  .tv-note {
    left: 272px; top: 488px; width: 248px;
    text-align: right; font-weight: 800; font-size: 12px; line-height: 16px;
  }
  .price-box {
    left: 305px; top: 530px; width: 217px; height: 150px;
    background: #fff; border-radius: 6px; overflow: hidden;
    box-shadow: 0 1px 4px rgba(0,0,0,.15);
  }
  .price-box h2 {
    background: var(--green); color: #fff;
    font-size: 11px; font-weight: 800; text-align: center;
    height: 24px; line-height: 24px; letter-spacing: .3px;
  }
  .lounge-photo {
    left: 40px; top: 520px; width: 255px; height: 190px;
    background: linear-gradient(180deg, #2f3238 0%, #4c5968 40%, #6b4a2f 62%, #9ea2a6 100%);
    clip-path: polygon(18% 0, 82% 0, 100% 20%, 100% 100%, 0 100%, 0 20%);
  }
  .contact {
    left: 40px; top: 722px; color: #fff; font-style: normal;
    font-weight: 700; font-size: 9.5px; line-height: 15px;
  }
  .contact p { display: flex; align-items: center; gap: 6px; }
</style>
</head>
<body>
<article class="flyer">
  <div class="hero-scene" role="img" aria-label="Green lawn and patio backdrop"></div>

  <svg class="curves" viewBox="0 0 540 764" aria-hidden="true">
    <path d="M0 0 H235 C260 100 240 175 0 210 Z" fill="#fff"/>
    <path d="M0 210 C240 175 260 100 235 0" fill="none" stroke="var(--orange)" stroke-width="6"/>
    <path d="M0 410 C160 400 300 340 540 260 V764 H0 Z" fill="var(--paper)"/>
    <path d="M0 410 C160 400 300 340 540 260" fill="none" stroke="var(--orange)" stroke-width="6"/>
    <path d="M0 702 C140 700 330 680 540 560 V764 H0 Z" fill="var(--orange)"/>
    <path d="M0 700 C140 698 330 678 540 556" fill="none" stroke="var(--green)" stroke-width="3"/>
  </svg>

  <div class="bar-photo" role="img" aria-label="Patio Perch Lounge bar with friends watching a game"></div>
  <div class="shelf-photo" role="img" aria-label="Close-up of bar shelves with bottles and glasses"></div>

  <div class="brand"><span class="brand-dot"></span>Brisk Meadow Builders</div>

  <h1 class="headline">
    <span class="g">Turn your back yard</span>
    <span class="o">into the ultimate</span>
    <span class="g">entertainment venue</span>
    <span class="o">with the stunning</span>
    <span class="g">Patio Perch Lounge!</span>
  </h1>

  <ul class="features">
    <li><svg width="14" height="14" viewBox="0 0 14 14"><circle cx="7" cy="7" r="7" fill="var(--green)"/><path d="M3.8 7.2 6 9.3 10.2 4.8" stroke="#fff" stroke-width="1.8" fill="none"/></svg>Entertain family &amp; friends in your very own back yard!</li>
    <li><svg width="14" height="14" viewBox="0 0 14 14"><circle cx="7" cy="7" r="7" fill="var(--green)"/><path d="M3.8 7.2 6 9.3 10.2 4.8" stroke="#fff" stroke-width="1.8" fill="none"/></svg>Available with or without solar and comes in a variety of colors</li>
  </ul>

  <p class="specs">Constructed with treated 4x4's, primed then painted with Thornby Calder best exterior paint for years of care free enjoyment. Also, Marlow Pendt Keystead shingles are dimensional, have a 25 year warranty and are rated for 150 mph winds!</p>

  <p class="tv-note">TV Mount included.<br>Shelves and TV are sold separately</p>

  <section class="price-box"><h2>PRICE LIST</h2></section>

  <div class="lounge-photo" role="img" aria-label="Patio Perch Lounge with guests at the bar and a dog resting nearby"></div>

  <address class="contact">
    <p><svg width="10" height="10" viewBox="0 0 10 10"><circle cx="5" cy="5" r="5" fill="var(--ink)"/><path d="M5 2.2a1.8 1.8 0 0 0-1.8 1.8C3.2 5.4 5 7.8 5 7.8S6.8 5.4 6.8 4A1.8 1.8 0 0 0 5 2.2Z" fill="#fff"/></svg>214 Larkfield Lane, Brookvale, SC 29000</p>
    <p><svg width="10" height="10" viewBox="0 0 10 10"><circle cx="5" cy="5" r="5" fill="var(--ink)"/><path d="M3 2.6 4.2 3.8 3.7 4.6C4.1 5.4 4.6 5.9 5.4 6.3L6.2 5.8 7.4 7 6.7 7.7C5 7.5 2.5 5 2.3 3.3Z" fill="#fff"/></svg>555-014-0288 &nbsp; www.briskmeadowbuilders.com</p>
  </address>
</article>
</body>
</html>
```